DL Flyer for vehicle buying/selling service and advice business

New business to help people sell their current vehicle then select and buy and maintain their next car. (New or used).
We'll prepare and sell your car for you and get $,000s more than a trade in.
Offer advice as to the best car currently on the market based on our customer's needs.
With country wide sourcing network of cars across all manufacturers we have great buying power to ensure the very best possible price.
Personal service, including preparation of car for sale, pickup of old and drop-off of new vehicles, organise RWC and any required repairs.
We are NOT a car dealer so we WILL not try to sell you the vehicles we own.
Totally impartial, professional and friendly service making the purchase of your next car a great experience.
Updates

Flyer wording===========“Don’t sell your car or buy your next car without speaking to us”We guarantee to get you a better price for your current car and to find a cheaper purchase price for your next car.With a country wide sourcing network of cars “new and used” across all manufacturers we have sensational buying power to ensure the very best possible price.We can source the right car on any budget, from $2,000 to $200,000We are NOT a car dealer so we WILL not try to sell you the vehicles we own.By not being affiliated with any individual car manufacturer or dealer we can offer absolute impartiality.We’ll sit with you to discuss the best car for your needs and even bring the car to you for a test drive without the pressure of a salesperson nearby.Our services include:• Selling your current car: - Obtaining a roadworthy certificate - Organising any repairs needed - Detailing your car (wash, vacuum, polish) - Advertising of your car - Dealing with potential buyers - Negotiating the best price on your behalf• Assisting with the selection of your next car• Organising test drives• Purchasing the car of your choice - Sourcing the very best price• Ongoing management of their vehicle (service, clean, repair)Possible inclusions in the flyer might be:Advantages of upgrading to a new vehicle include:o reliability, o safety,o fuel efficiencyo comfort.Space for a couple of short testimonials Background images of all of the major car manufacturers Added Friday, July 29, 2016

Target Market(s)

Local community.
Initially will drop DL flyers in local post boxes

Industry/Entity Type

Business

Requirements
Must have
• Flyer wording:
• ===========
• “Don’t sell your car or buy your next car without speaking to us”
• ---------------------------------------------------------------------------------
• We guarantee to get you a better price for your current car and to find a cheaper purchase price for your next car.
• With a country wide sourcing network of cars “new and used” across all manufacturers we have sensational buying power to ensure the very best possible price.
• We can source the right car on any budget, from $2,000 to $200,000
• We are NOT a car dealer so we WILL not try to sell you the vehicles we own.
• By not being affiliated with any individual car manufacturer or dealer we can offer absolute impartiality.
• We’ll sit with you to discuss the best car for your needs and even bring the car to you for a test drive without the pressure of a salesperson nearby.
• Our services include:
• • Selling your current car:
• o Obtaining a roadworthy certificate
• o Organising any repairs needed
• o Detailing your car (wash, vacuum, polish)
• o Advertising of your car
• o Dealing with potential buyers
• o Negotiating the best price on your behalf
• • Assisting with the selection of your next car
• • Organising test drives
• • Purchasing the car of your choice
• o Sourcing the very best price
• • Ongoing management of your vehicle (service, clean, repair)
• Call Gerald on: 0427 315064
Nice to have
• Possible inclusions on the flyer might be:
• List of advantages of upgrading to a new vehicle:
• o reliability,
• o safety,
• o fuel efficiency
• o comfort
• Space for a couple of short testimonials
• Background images of all of the major car manufacturers

```html
<!DOCTYPE html>
<html lang="en">
<head>
<meta charset="utf-8">
<title>FairWheels DL Flyer</title>
<link href="https://fonts.googleapis.com/css2?family=Bebas+Neue&family=Barlow:wght@400;500;700;800&display=swap" rel="stylesheet">
<style>
  :root{
    --yellow:#fdc325;
    --yellow-deep:#f6b417;
    --orange-top:#ffb02e;
    --orange-bottom:#f08a14;
    --black:#111111;
    --ink:#1b1b1b;
    --grey-bg:#e6e6e6;
    --pattern-dark:#2a2a2a;
    --pattern-light:#ececec;
    --white:#ffffff;
  }
  *{margin:0;padding:0;box-sizing:border-box}
  html,body{width:900px;height:1200px;overflow:hidden}
  body{background:var(--grey-bg);position:relative;font-family:'Barlow',Arial,sans-serif;color:var(--ink)}
  .flyer{position:absolute;top:183px;width:406px;height:837px;overflow:hidden;box-shadow:0 2px 6px rgba(0,0,0,.25)}
  .flyer--front{left:38px;background:var(--white)}
  .flyer--back{left:455px;background:var(--pattern-light)}
  .abs{position:absolute}

  /* front */
  .brand-wall{left:0;top:0;width:406px;height:380px;background:linear-gradient(180deg,#1c1c1c,#3a3a3a 60%,#4a4a4a)}
  .family-photo{left:0;top:195px;width:406px;height:370px;background:linear-gradient(180deg,#8a8f86 0%,#6e7a5e 45%,#4d5a3e 75%,#7b7a6e 100%)}
  .photo-edge{left:0;top:520px}
  .headline{left:0;top:33px;width:406px;text-align:center;font-family:'Bebas Neue',Impact,sans-serif;font-size:45px;line-height:44px;background:linear-gradient(180deg,var(--orange-top),var(--orange-bottom));-webkit-background-clip:text;background-clip:text;color:transparent}
  .guarantee{left:26px;top:558px;width:360px;font-size:14px;line-height:18px;font-weight:500;text-transform:uppercase}
  .guarantee .hl{color:var(--yellow-deep);font-weight:700}
  .guarantee strong{font-weight:700}
  .network{left:26px;top:625px;width:362px;font-size:12.5px;line-height:17px}
  .network strong{font-weight:700}
  .hazard{left:0;width:406px;height:14px;background:repeating-linear-gradient(-45deg,var(--black) 0 7px,var(--yellow) 7px 14px)}
  .hazard--light{background:repeating-linear-gradient(-45deg,var(--white) 0 7px,var(--black) 7px 14px)}
  .contact{left:0;top:712px;width:406px;height:125px}
  .contact--front{background:var(--yellow);color:var(--black)}
  .contact--back{background:linear-gradient(180deg,#222,#000);color:var(--yellow)}
  .call{position:absolute;left:0;top:20px;width:100%;text-align:center;font-weight:700;font-size:31px;line-height:38px;letter-spacing:.5px;display:flex;justify-content:center;align-items:center;gap:6px}
  .call svg{width:28px;height:28px}
  .brand{position:absolute;left:0;top:58px;width:100%;display:flex;justify-content:center;align-items:center;gap:10px}
  .brand-mark{width:44px;height:26px;border:2px solid currentColor;border-radius:3px}
  .brand-name{font-weight:800;font-size:35px;line-height:40px;letter-spacing:.5px}

  /* back */
  .brand-grid-warm{left:0;top:0;width:406px;height:405px;background:linear-gradient(180deg,var(--yellow) 0%,var(--yellow-deep) 100%)}
  .brand-grid-cool{left:0;top:405px;width:406px;height:295px;background:linear-gradient(180deg,#f3f3f3,#e2e2e2)}
  .dealer-title{left:0;top:30px;width:406px;text-align:center;font-weight:800;font-size:27px;line-height:30px;color:var(--black)}
  .dealer-sub{left:0;top:60px;width:406px;text-align:center;font-weight:700;font-size:12px;line-height:14px;color:var(--black)}
  .dealer-copy{left:22px;width:362px;text-align:center;font-size:12.5px;line-height:16px;color:var(--black)}
  .services-card{left:24px;top:197px;width:358px;height:268px;background:var(--white);border-radius:6px;box-shadow:0 1px 5px rgba(0,0,0,.25)}
  .services-banner{left:45px;top:180px}
  .services-title{left:45px;top:180px;width:316px;height:38px;line-height:38px;text-align:center;color:var(--yellow);font-weight:700;font-size:18px;letter-spacing:.4px}
  .service-list{left:56px;top:222px;width:320px;list-style:none}
  .service-list>li{position:relative;font-weight:700;font-size:13px;line-height:17px;margin-bottom:5px}
  .service-list>li svg{position:absolute;left:-22px;top:2px;width:13px;height:13px}
  .service-list ul{list-style:none;font-weight:400;font-size:11.5px;line-height:15.3px;padding-left:14px;margin-top:1px}
  .service-list ul li::before{content:"• "}
  .service-note{font-weight:400;font-size:11.5px;line-height:14px;display:block}
  .reviews-title{left:0;top:483px;width:406px;text-align:center;font-weight:700;font-size:18.5px;color:var(--black)}
  .client-photo{left:25px;width:95px;height:74px;border-radius:5px;background:linear-gradient(160deg,#c9cdd1,#8c8f94 60%,#5f6166)}
  .review{left:128px;width:262px;text-align:center;font-size:12px;line-height:15px;color:var(--black)}
  .review cite{display:block;font-style:normal;margin-top:5px}
  .review cite strong{font-weight:700}
</style>
</head>
<body>

<section class="flyer flyer--front">
  <div class="abs brand-wall" role="img" aria-label="Wall of car manufacturer emblems on a dark checkered backdrop"></div>
  <div class="abs family-photo" role="img" aria-label="Photo of grandparents, two girls and a golden retriever sitting in the open boot of a white car"></div>
  <svg class="abs photo-edge" width="406" height="50" viewBox="0 0 406 50"><path d="M0 42 H265 C295 42 300 18 330 18 H406 V50 H0 Z" fill="#ffffff"/></svg>
  <h1 class="abs headline">Before you sell your car<br>or buy your next car<br>speak to us!</h1>
  <p class="abs guarantee">We guarantee <span class="hl">to get you<br>a better price</span> for your current car and to find <strong>a cheaper purchase price</strong> for your next car</p>
  <p class="abs network">With a country wide sourcing network of cars <strong>“new and used”</strong> across all manufacturers we have sensational buying power to ensure the very best possible price.</p>
  <div class="abs hazard" style="top:698px"></div>
  <div class="abs contact contact--front">
    <div class="call">CALL
      <svg viewBox="0 0 28 28"><circle cx="14" cy="14" r="12" fill="none" stroke="currentColor" stroke-width="2.4"/><path d="M10 8.5c-1 .6-1.6 1.6-1.3 3 .9 3.6 3.6 6.4 7.2 7.3 1.3.3 2.4-.3 3-1.3l-2.2-1.8-1.4 1c-1.8-.8-3.2-2.2-4-4l1-1.4z" fill="currentColor"/></svg>
      0427 315064</div>
    <div class="brand"><span class="brand-mark"></span><span class="brand-name">FAIRWHEELS</span></div>
  </div>
</section>

<section class="flyer flyer--back">
  <div class="abs brand-grid-warm" role="img" aria-label="Faint grid of car manufacturer emblems on yellow"></div>
  <div class="abs brand-grid-cool" role="img" aria-label="Faint grid of car manufacturer emblems on light grey"></div>
  <h2 class="abs dealer-title">WE ARE NOT A CAR DEALER</h2>
  <p class="abs dealer-sub">SO WE WILL NOT TRY TO SELL YOU THE VEHICLES WE OWN</p>
  <p class="abs dealer-copy" style="top:86px">By not being affiliated with any individual car manufacturer or dealer we can offer absolute impartiality.</p>
  <p class="abs dealer-copy" style="top:122px">We’ll sit with you to discuss the best car for your needs and even bring the car to you for a test drive without the pressure of a salesperson nearby.</p>

  <div class="abs services-card"></div>
  <svg class="abs services-banner" width="316" height="38" viewBox="0 0 316 38"><path d="M14 0 H302 L316 8 L298 38 H18 L0 8 Z" fill="#111"/></svg>
  <h3 class="abs services-title">OUR SERVICES INCLUDE</h3>
  <ul class="abs service-list">
    <li><svg viewBox="0 0 13 13"><circle cx="6.5" cy="6.5" r="5.5" fill="none" stroke="#111" stroke-width="1.5"/><path d="M3.8 6.6l2 2 3.8-4.2" fill="none" stroke="#111" stroke-width="1.7"/></svg>Selling your current car:
      <ul>
        <li>Obtaining a roadworthy certificate</li>
        <li>Organising any repairs needed</li>
        <li>Detailing your car (wash, vacuum, polish)</li>
        <li>Advertising of your car</li>
        <li>Dealing with potential buyers</li>
        <li>Negotiating the best price on your behalf</li>
      </ul>
    </li>
    <li><svg viewBox="0 0 13 13"><circle cx="6.5" cy="6.5" r="5.5" fill="none" stroke="#111" stroke-width="1.5"/><path d="M3.8 6.6l2 2 3.8-4.2" fill="none" stroke="#111" stroke-width="1.7"/></svg>Assisting with the selection of your next car</li>
    <li><svg viewBox="0 0 13 13"><circle cx="6.5" cy="6.5" r="5.5" fill="none" stroke="#111" stroke-width="1.5"/><path d="M3.8 6.6l2 2 3.8-4.2" fill="none" stroke="#111" stroke-width="1.7"/></svg>Organising test drives</li>
    <li><svg viewBox="0 0 13 13"><circle cx="6.5" cy="6.5" r="5.5" fill="none" stroke="#111" stroke-width="1.5"/><path d="M3.8 6.6l2 2 3.8-4.2" fill="none" stroke="#111" stroke-width="1.7"/></svg>Purchasing the car of your choice
      <ul><li>Sourcing the very best price</li></ul>
    </li>
    <li><svg viewBox="0 0 13 13"><circle cx="6.5" cy="6.5" r="5.5" fill="none" stroke="#111" stroke-width="1.5"/><path d="M3.8 6.6l2 2 3.8-4.2" fill="none" stroke="#111" stroke-width="1.7"/></svg>Ongoing management of your vehicle
      <span class="service-note">(service, clean, repair)</span></li>
  </ul>

  <h3 class="abs reviews-title">WHAT OUR CLIENTS SAY</h3>
  <div class="abs client-photo" style="top:515px" role="img" aria-label="Photo of a smiling woman and child beside a car"></div>
  <blockquote class="abs review" style="top:519px">Lorem ipsum dolor sit amet, consectetur adipiscing elit. Fusce ut diam ut nunc efficitur sodales at sit amet metus.<cite>~ <strong>Client name</strong>, Lorem ipsum</cite></blockquote>
  <div class="abs client-photo" style="top:598px" role="img" aria-label="Photo of a smiling woman holding car keys in a car"></div>
  <blockquote class="abs review" style="top:602px">Lorem ipsum dolor sit amet, consectetur adipiscing elit. Fusce ut diam ut nunc efficitur sodales at sit amet metus.<cite>~ <strong>Client name</strong>, Lorem ipsum</cite></blockquote>

  <div class="abs hazard hazard--light" style="top:700px;background:repeating-linear-gradient(-45deg,var(--yellow) 0 7px,var(--white) 7px 14px)"></div>
  <div class="abs contact contact--back" style="top:714px">
    <div class="call">CALL
      <svg viewBox="0 0 28 28"><circle cx="14" cy="14" r="12" fill="none" stroke="currentColor" stroke-width="2.4"/><path d="M10 8.5c-1 .6-1.6 1.6-1.3 3 .9 3.6 3.6 6.4 7.2 7.3 1.3.3 2.4-.3 3-1.3l-2.2-1.8-1.4 1c-1.8-.8-3.2-2.2-4-4l1-1.4z" fill="currentColor"/></svg>
      0427 315064</div>
    <div class="brand"><span class="brand-mark"></span><span class="brand-name">FAIRWHEELS</span></div>
  </div>
</section>

</body>
</html>
```